Verostel business card

Business card for sustainable investment company called "Verostel". Verostel is an exchange platform selling carbon credits between buyers and sellers. Carbon Credits are an environmental commodity for reducing global carbon emissions.

the card should obviously have our logo and the theme should be sustainability/environment mixed with a trading platform.

Contact Information for Business Card

Logo, Name, Title, Phone, Email

Colors
0054AA
0677BA
7BADD7
CADEEF
E8F1F8
0094D4
00A9DD
6FCCEA
C7EBF8
E9F6FB
00AB8E
00BBA5
67D7C9
C6EFE9
E9F9F6
59FF00
82FF00
B8FF75
E3FFCB
F4FFEA

```html
<!DOCTYPE html>
<html lang="en">
<head>
<meta charset="utf-8">
<title>Verostel business card</title>
<link rel="stylesheet" href="https://fonts.googleapis.com/css2?family=Lato:wght@700;900&family=Roboto:wght@300;400&display=swap">
<style>
  :root {
    --bg: #8f8f8f;
    --navy: #1d2b45;
    --sky: #3aaee2;
    --azure: #4a9fd6;
    --royal: #4272bc;
    --aqua: #66cad8;
    --white: #ffffff;
    --ink: #2a3346;
  }
  * { margin: 0; padding: 0; box-sizing: border-box; }
  html, body { width: 1067px; height: 1200px; overflow: hidden; }
  body {
    background: var(--bg);
    display: flex;
    flex-direction: column;
    align-items: center;
    justify-content: center;
    gap: 60px;
  }
  .card {
    position: relative;
    width: 880px;
    height: 503px;
    overflow: hidden;
    box-shadow: 0 3px 6px rgba(0,0,0,0.35);
  }

  /* Front */
  .card-front { background: var(--white); }
  .front-band {
    position: absolute;
    left: 0; top: 0;
    width: 230px; height: 100%;
    background: linear-gradient(90deg, var(--sky), var(--royal));
  }
  .edge-tab {
    position: absolute;
    right: 0; top: 260px;
    width: 14px; height: 212px;
    border-radius: 12px 0 0 12px;
    background: linear-gradient(180deg, var(--royal), var(--sky));
  }
  .brand {
    position: absolute;
    display: flex;
    align-items: center;
    gap: 18px;
    font-family: "Lato", sans-serif;
    font-weight: 900;
    font-size: 56px;
    letter-spacing: 1px;
    text-transform: uppercase;
    line-height: 1;
  }
  .brand-mark { width: 52px; height: 52px; }
  .card-front .brand { right: 50px; top: 58px; color: var(--navy); }
  .card-front .brand-mark { background: var(--azure); }

  .contact {
    position: absolute;
    right: 50px;
    top: 265px;
    text-align: right;
  }
  .person-name {
    font-family: "Lato", sans-serif;
    font-weight: 700;
    font-size: 58px;
    line-height: 1;
    color: var(--azure);
  }
  .person-title {
    font-family: "Roboto", sans-serif;
    font-weight: 400;
    font-size: 29px;
    color: var(--ink);
    margin-top: 2px;
  }
  .contact-line {
    display: flex;
    justify-content: flex-end;
    align-items: center;
    gap: 10px;
    font-family: "Roboto", sans-serif;
    font-weight: 300;
    font-size: 25px;
    color: var(--ink);
    margin-top: 14px;
  }
  .contact-line + .contact-line { margin-top: 8px; }
  .contact-icon { width: 16px; height: 16px; fill: var(--royal); }

  /* Back */
  .card-back {
    background: linear-gradient(90deg, var(--sky) 0%, var(--aqua) 28%, var(--royal) 78%, var(--royal) 100%);
  }
  .card-back .brand { right: 51px; top: 389px; color: var(--white); }
  .card-back .brand-mark { background: var(--white); }
</style>
</head>
<body>

  <section class="card card-front">
    <div class="front-band"></div>
    <div class="edge-tab"></div>
    <div class="brand"><span class="brand-mark"></span><span class="brand-name">Verostel</span></div>
    <div class="contact">
      <p class="person-name">Your Namehere</p>
      <p class="person-title">Your Title</p>
      <p class="contact-line">012 345 6789
        <svg class="contact-icon" viewBox="0 0 16 16" aria-hidden="true"><path d="M4 1h3l1 4-2 1.5c.8 2 2 3.3 3.5 4.5L11 9l4 1v3c0 1-1 2-2 2C6.5 15 1 9.5 1 3c0-1 1-2 3-2z"/></svg>
      </p>
      <p class="contact-line">youremail@email.com
        <svg class="contact-icon" viewBox="0 0 16 16" aria-hidden="true"><path d="M1 3h14v10H1z"/><path d="M1 3l7 6 7-6" fill="none" stroke="#fff" stroke-width="1.5"/></svg>
      </p>
    </div>
  </section>

  <section class="card card-back">
    <div class="brand"><span class="brand-mark"></span><span class="brand-name">Verostel</span></div>
  </section>

</body>
</html>
```